KPV Construction we build lodges in Botswana

We need a Design Layout only with Categories where we can update each projects photos.... We have a web address and a host - kpv.construction

```html
<!DOCTYPE html>
<html lang="en">
<head>
<meta charset="utf-8">
<title>KPV Construction</title>
<link rel="stylesheet" href="https://fonts.googleapis.com/css2?family=Oswald:wght@300;400;500&family=Montserrat:wght@400;500;600&family=Roboto:wght@400;500&display=swap">
<style>
  :root {
    --red: #f20d0d;
    --navy: #0b3a78;
    --navy-deep: #072c5e;
    --blue: #1769c2;
    --night: #13246e;
    --ink: #1b1b1b;
    --grey-bg: #ececee;
    --text: #444;
    --white: #fff;
    --dark-panel: #232323;
  }
  * { margin: 0; padding: 0; box-sizing: border-box; }
  html, body { width: 1200px; height: 2514px; overflow: hidden; }
  body { position: relative; background: var(--white); font-family: "Montserrat", sans-serif; color: var(--text); }
  .abs { position: absolute; }

  /* Hero */
  .hero { position: absolute; left: 0; top: 0; width: 1200px; height: 717px; }
  .hero-photo { position: absolute; left: 62px; top: 0; width: 1138px; height: 717px;
    background: radial-gradient(ellipse at 60% 75%, #2f7a3a 0%, rgba(47,122,58,0) 45%),
                linear-gradient(180deg, #0f2a8c 0%, #1a3fa0 45%, #16306b 75%, #0d1d3b 100%); }
  .hero-strip { position: absolute; left: 0; top: 0; width: 62px; height: 717px; background: var(--red); }
  .brand { position: absolute; left: 92px; top: 60px; display: flex; align-items: center; gap: 10px;
    font-family: "Montserrat", sans-serif; font-weight: 600; font-size: 22px; color: var(--white); letter-spacing: 1px; }
  .brand-mark { width: 22px; height: 22px; background: var(--red); }
  .hero-phone { position: absolute; left: 892px; top: 47px; display: flex; align-items: center; gap: 14px;
    color: var(--white); font-weight: 600; font-size: 17px; letter-spacing: .5px; }
  .hero-menu { position: absolute; left: 1096px; top: 40px; color: var(--white); font-size: 11px; text-align: center; }
  .hero-menu span { display: block; width: 28px; height: 2px; background: var(--white); margin: 4px auto 0; }
  .hero-title { position: absolute; left: 156px; top: 258px; font-family: "Oswald", sans-serif; font-weight: 500;
    font-size: 60px; color: var(--white); letter-spacing: .5px; }
  .hero-text { position: absolute; left: 156px; top: 356px; width: 650px; color: var(--white); font-size: 15px; line-height: 25px; }
  .btn { position: absolute; top: 486px; height: 40px; display: flex; align-items: center; justify-content: center;
    color: var(--white); font-size: 14px; font-weight: 500; }
  .btn-outline { left: 176px; width: 147px; border: 1.5px solid var(--white); }
  .btn-solid { left: 344px; width: 146px; background: var(--red); border: 1.5px solid #ff6b6b; }
  .social-side { position: absolute; left: 14px; width: 27px; height: 27px; border: 1.5px solid var(--white); border-radius: 50%; }
  .slider-arrow { position: absolute; top: 608px; width: 40px; height: 40px; background: var(--white); }

  /* About */
  .about { position: absolute; left: 0; top: 717px; width: 1200px; height: 800px; background: var(--grey-bg); }
  .about-photo { position: absolute; left: 67px; top: 821px; width: 427px; height: 429px;
    background: linear-gradient(160deg, #5a4a3c 0%, #8b7566 40%, #b9b2a4 65%, #4e5a4c 100%); }
  .experience { position: absolute; left: 80px; top: 810px; width: 222px; height: 103px; background: var(--ink);
    color: var(--white); display: flex; align-items: center; padding-left: 30px; gap: 12px; }
  .experience b { font-size: 34px; font-weight: 500; }
  .experience small { font-size: 13px; font-weight: 600; }
  .play { position: absolute; left: 466px; top: 1007px; width: 54px; height: 54px; border-radius: 50%; background: var(--ink); }
  .welcome { position: absolute; left: 563px; top: 864px; font-family: "Oswald", sans-serif; font-weight: 300; font-size: 21px; color: #333; }
  .about-title { position: absolute; left: 563px; top: 888px; font-family: "Oswald", sans-serif; font-weight: 400; font-size: 46px; color: #555; }
  .about-title em { font-style: normal; color: var(--blue); }
  .about-rule { position: absolute; left: 566px; top: 953px; width: 80px; height: 3px; background: var(--blue); }
  .about-text { position: absolute; left: 568px; top: 975px; width: 540px; font-size: 14.5px; line-height: 28px; color: #555; }
  .stat { position: absolute; top: 1132px; }
  .stat b { display: block; font-size: 34px; font-weight: 500; color: var(--ink); }
  .stat span { display: block; margin-top: 30px; font-size: 14.5px; color: #444; }

  /* Projects */
  .projects { position: absolute; left: 0; top: 1404px; width: 1200px; height: 802px;
    background: linear-gradient(180deg, var(--navy) 0%, var(--navy-deep) 100%);
    clip-path: polygon(0 0, 100% 78px, 100% 100%, 0 100%); }
  .projects-title { position: absolute; left: 0; width: 1200px; top: 1506px; text-align: center;
    font-family: "Oswald", sans-serif; font-size: 46px; color: var(--white); }
  .projects-title em { font-style: normal; color: var(--blue); }
  .filters { position: absolute; top: 1588px; left: 382px; display: flex; gap: 0; font-size: 15px; color: var(--white); }
  .filters span { padding: 6px 14px; }
  .filters .active { background: var(--blue); }
  .tile { position: absolute; }
  .nav-arrow { position: absolute; top: 2145px; }

  /* Footer */
  .footer-rule { position: absolute; left: 0; top: 2212px; width: 1200px; height: 2px; background: #e4e4e4; }
  .footer-brand { position: absolute; left: 60px; top: 2340px; display: flex; align-items: center; gap: 10px;
    font-weight: 600; font-size: 22px; color: var(--blue); letter-spacing: 1px; }
  .footer-brand i { width: 22px; height: 22px; background: var(--red); }
  .copyright { position: absolute; left: 20px; top: 2430px; font-family: "Roboto", sans-serif; font-size: 15px; color: #666; }
  .footer-col { position: absolute; top: 2286px; list-style: none; font-family: "Roboto", sans-serif; font-size: 15px; color: var(--ink); }
  .footer-col li { height: 34px; }
  .footer-social { position: absolute; left: 1064px; top: 2241px; width: 74px; height: 268px; background: var(--dark-panel);
    display: flex; flex-direction: column; align-items: center; justify-content: space-around; padding: 10px 0; }
  .footer-social i { width: 18px; height: 18px; border: 1.5px solid #bbb; border-radius: 50%; }
</style>
</head>
<body>

<section class="hero">
  <div class="hero-photo" role="img" aria-label="Construction site at dusk with tower cranes and scaffolding under a deep blue sky"></div>
  <div class="hero-strip"></div>
  <div class="brand"><i class="brand-mark"></i>KPV CONSTRUCTION</div>
  <div class="hero-phone">
    <svg width="12" height="20" viewBox="0 0 12 20"><rect x="1" y="1" width="10" height="18" rx="2" fill="none" stroke="#fff" stroke-width="1.6"/><circle cx="6" cy="15.5" r="1" fill="#fff"/></svg>
    1800-555-0147
  </div>
  <div class="hero-menu">MENU<span></span><span></span><span></span></div>
  <h1 class="hero-title">WE BUILD BIG THINGS FOR YOU</h1>
  <p class="hero-text">Lorem Ipsum is simply dummy text of the printing and typesetting industry. Lorem Ipsum has been the industry's standard dummy text ever since the 1500s, when an unknown printer took a galley of type and scrambled</p>
  <a class="btn btn-outline">Get Started</a>
  <a class="btn btn-solid">Contact Us</a>
  <i class="social-side" style="top:443px"></i>
  <i class="social-side" style="top:496px"></i>
  <i class="social-side" style="top:547px"></i>
  <i class="social-side" style="top:595px"></i>
  <i class="social-side" style="top:646px"></i>
  <div class="slider-arrow" style="left:1042px"><svg width="40" height="40"><path d="M23 15 L16 20 L23 25 Z" fill="#111"/></svg></div>
  <div class="slider-arrow" style="left:1089px"><svg width="40" height="40"><path d="M17 15 L24 20 L17 25 Z" fill="#111"/></svg></div>
</section>

<section class="about"></section>
<div class="about-photo" role="img" aria-label="Modern angular building with glass facade beside a reflecting pool"></div>
<div class="experience"><b>15</b><small>Years Experience</small></div>
<div class="play"><svg width="54" height="54"><path d="M23 21 L33 27 L23 33 Z" fill="#fff"/></svg></div>
<div class="welcome">WELCOME TO</div>
<h2 class="about-title"><em>KPV</em> CONSTRUCTION</h2>
<div class="about-rule"></div>
<p class="about-text">Lorem ipsum dolor sit amet, consectetur adipisicing elit. Quae et corporis vero dicta praesentium, odio tenetur iusto porro veniam rerum Lorem ipsum dolor sit amet, consectetur adipisicing elit. Minima, facilis. Lorem ipsum dolor sit amet, consectetur adipisicing elit. Atque ipsum sint esse. Repellendus rerum, expedita.</p>
<div class="stat" style="left:575px"><b>49</b><span>Business Partners</span></div>
<div class="stat" style="left:771px"><b>455</b><span>Projects Completed</span></div>
<div class="stat" style="left:965px"><b>30</b><span>Trusted Consultent</span></div>

<section class="projects"></section>
<h2 class="projects-title">OUR <em>PROJECTS</em></h2>
<div class="filters"><span class="active">All</span><span>Restaurants</span><span>Buildings</span><span>Apartments</span><span>Residence</span></div>

<div class="tile" style="left:7px;top:1648px;width:338px;height:224px;background:linear-gradient(180deg,#7fb4e6,#9bb7c8 55%,#6a8a4a)" role="img" aria-label="Glass office buildings with trees along a walkway"></div>
<div class="tile" style="left:355px;top:1648px;width:337px;height:224px;background:linear-gradient(180deg,#3c4a78,#6d5a48 60%,#c79a5a)" role="img" aria-label="Modern house lit warmly at dusk"></div>
<div class="tile" style="left:702px;top:1648px;width:339px;height:224px;background:linear-gradient(180deg,#4f7fc0,#9fb8cf 50%,#4a4a3a)" role="img" aria-label="Angular glass office building under a blue sky"></div>
<div class="tile" style="left:1051px;top:1648px;width:149px;height:224px;background:linear-gradient(180deg,#6e9ad0,#a7b8c6 60%,#5b6470)" role="img" aria-label="Glass tower facade"></div>
<div class="tile" style="left:7px;top:1882px;width:330px;height:218px;background:linear-gradient(180deg,#3f7fd0,#a3b4bf 55%,#6b7b5a)" role="img" aria-label="City office blocks with landscaped plaza"></div>
<div class="tile" style="left:347px;top:1882px;width:330px;height:218px;background:linear-gradient(180deg,#cfc8c0,#8d7a68 55%,#5b4c40)" role="img" aria-label="Workers tying steel reinforcement on a site"></div>
<div class="tile" style="left:687px;top:1882px;width:329px;height:218px;background:linear-gradient(180deg,#1f3d80,#38508a 50%,#c9b08a 75%,#8fb7d6)" role="img" aria-label="Villa with pool terrace at night"></div>
<div class="tile" style="left:1026px;top:1882px;width:174px;height:218px;background:linear-gradient(180deg,#2d4e8c,#5a5550 60%,#3d3a33)" role="img" aria-label="Stone wall building lit at dusk"></div>

<svg class="nav-arrow" style="left:566px" width="37" height="14"><path d="M1 7 H36 M1 7 L8 2 M1 7 L8 12" stroke="#fff" stroke-width="2" fill="none"/></svg>
<svg class="nav-arrow" style="left:628px" width="37" height="14"><path d="M0 7 H36 M36 7 L29 2 M36 7 L29 12" stroke="#fff" stroke-width="2" fill="none"/></svg>

<footer>
  <div class="footer-rule"></div>
  <div class="footer-brand"><i></i>KPV CONSTRUCTION</div>
  <p class="copyright">Copyright © 2019 All rights reserved.</p>
  <ul class="footer-col" style="left:389px"><li>Home</li><li>About us</li><li>Services</li><li>Portfolio</li><li>Blog</li></ul>
  <ul class="footer-col" style="left:583px"><li>Terms &amp; Conditions</li><li>FAQ</li><li>Help Desk</li><li>Job Aplications</li><li>Site Map</li></ul>
  <ul class="footer-col" style="left:838px"><li>Privacy</li><li>Contact us</li><li>Newsletter</li><li>Clients Testimonials</li><li>FAQ</li></ul>
  <div class="footer-social"><i></i><i></i><i></i><i></i><i></i></div>
</footer>

</body>
</html>
```